Attention Getting Doorhanger Postcard Campaign offering HUGE Rebate on New Construction Homes

I am reestablishing my real estate career in the far North Dallas, TX area and want to offer a rebate on new construction homes to help get me started. I am requesting a doorhanger as my first project but would like a theme that I can carry over to other projects including postcards and other marketing items. I want it to look high end, clean, professional and classy. I am attaching a copy of a flier that I created that needs (no graphic designer here) some prettying up. But this is just to give you an idea of the type of style that is of interest to me.

Target Market(s)

Home buyers for new construction in far north dallas suburbs. Usually a move up buyer.

Industry/Entity Type

Real Estate

Colors

Designer to choose colors to be used in the design.

Requirements
Must have
• Catch phrase, draw attention, classy clean lines, current trend colors of blues and grays. My information, Harwood Fenn logo, equal housing and realtor logos. Fine Print: Not intended to solicit homes already listed for sale or buyers already in a buyers agency agreement with another brokerage. Please include offer details as listed in my flier. Again I am interested in a door hanger and the next round would be a flier or postcard.
Nice to have
• Picture of new homes that are in line with what is being built in my area. A few home builders sites: Silver Meadow, Brookvale Homes, Tenbury Homes, Calloway Homes.

```html
<!DOCTYPE html>
<html lang="en">
<head>
<meta charset="utf-8">
<title>Dana Whitcombe – New Construction Rebate Door Hanger</title>
<link rel="stylesheet" href="https://fonts.googleapis.com/css2?family=Montserrat:ital,wght@0,400;0,600;0,700;0,800;1,700&family=Arimo:wght@400;700&family=Satisfy&display=swap">
<style>
  :root{
    --page:#e6e8ec;
    --royal:#1a5fb4;
    --royal-deep:#0b3f8f;
    --sky-top:#9cc8ee;
    --sky-bottom:#ffffff;
    --ink:#1b1d22;
    --slate:#4b5563;
    --white:#ffffff;
    --accent-red:#b40f1e;
  }
  *{box-sizing:border-box;margin:0;padding:0}
  html,body{width:1200px;height:1000px;overflow:hidden}
  body{background:var(--page);font-family:"Arimo",Arial,sans-serif;color:var(--ink);position:relative}

  .hanger{position:absolute;top:65px;width:350px;height:870px;background:var(--white);overflow:hidden;box-shadow:0 6px 18px rgba(0,0,0,.18)}
  .hanger--front{left:235px}
  .hanger--back{left:615px}
  .hanger__hole{position:absolute;width:84px;height:84px;border-radius:50%;background:var(--page);top:108px}
  .hanger--front .hanger__hole{left:173px}
  .hanger--back .hanger__hole{left:83px}
  .hanger__slit{position:absolute;top:0;width:6px;height:108px;background:var(--page)}
  .hanger--front .hanger__slit{left:212px}
  .hanger--back .hanger__slit{left:122px}

  /* front */
  .front__sky{position:absolute;left:0;top:0;width:100%;height:215px;background:linear-gradient(180deg,var(--royal-deep),var(--royal) 70%,#3f86d6)}
  .photo{position:absolute;left:0;width:100%}
  .photo--brick{top:215px;height:190px;background:linear-gradient(180deg,#3f7ac4 0%,#8d7f73 45%,#6c6256 70%,#4f7a3a 100%)}
  .photo--grey{top:410px;height:166px;background:linear-gradient(180deg,#b9a7a0 0%,#9a9da3 50%,#6f7378 80%,#4d6a3c 100%)}
  .photo--white{top:581px;height:145px;background:linear-gradient(180deg,#d7c8be 0%,#e9e6e2 50%,#8f9a86 100%)}
  .divider{position:absolute;left:0;width:100%;height:5px;background:var(--royal)}
  .divider--one{top:405px}
  .divider--two{top:576px}

  .headline{position:absolute;left:0;top:330px;width:100%;font-family:"Montserrat",sans-serif;color:var(--white);text-shadow:0 2px 6px rgba(0,0,0,.55)}
  .headline__awe{position:absolute;left:28px;top:0;font-size:40px;font-weight:800;letter-spacing:1px}
  .headline__and{position:absolute;left:135px;top:2px;font-size:15px;font-weight:700;font-style:italic}
  .headline__some{position:absolute;left:155px;top:20px;font-size:40px;font-weight:800;letter-spacing:1px}

  .agent-panel{position:absolute;left:0;top:726px;width:100%;height:144px;background:var(--white)}
  .agent-photo{position:absolute;left:0;top:680px;width:150px;height:190px;background:linear-gradient(180deg,#6b4a36 0%,#c89e84 40%,#1c2742 65%,#18213a 100%);border-top-right-radius:70px}
  .agent__name{position:absolute;left:158px;top:733px;font-family:"Satisfy",cursive;font-size:22px;line-height:1.2;color:var(--ink);white-space:nowrap}
  .agent__creds{position:absolute;left:158px;top:766px;font-family:"Montserrat",sans-serif;font-size:9.5px;font-weight:600;line-height:1.4;color:var(--ink);white-space:nowrap}
  .agent__badges{position:absolute;left:298px;top:779px;display:flex;gap:6px}
  .badge{width:16px;height:16px;background:var(--ink)}
  .brand{display:flex;align-items:center;gap:6px;font-family:"Montserrat",sans-serif;font-weight:700;color:var(--accent-red);white-space:nowrap}
  .brand__mark{width:12px;height:12px;background:var(--accent-red)}
  .front__brand{position:absolute;left:180px;top:804px;font-size:13px}
  .front__contact{position:absolute;left:178px;top:826px;font-family:"Montserrat",sans-serif;font-weight:700;font-size:12px;line-height:1.45;color:var(--ink);white-space:nowrap}
  .front__contact .phone{font-size:14px}

  /* back */
  .back__sky{position:absolute;left:0;top:0;width:100%;height:300px;background:linear-gradient(180deg,var(--sky-top) 0%,#cfe3f5 55%,var(--sky-bottom) 100%)}
  .back__content{position:absolute;left:0;top:0;width:100%;font-family:"Montserrat",sans-serif}
  .offer__lead{position:absolute;left:0;top:218px;width:100%;text-align:center;font-size:17px;font-weight:600}
  .offer__rate{position:absolute;left:14px;top:236px;font-size:44px;font-weight:800;color:var(--royal);letter-spacing:-1px}
  .offer__detail{position:absolute;left:128px;top:246px;font-size:12.5px;font-weight:600;line-height:1.2}
  .offer__detail b{color:var(--royal);font-weight:800}
  .banner{position:absolute;left:12px;top:300px;padding:3px 10px;background:var(--royal);color:var(--white);font-size:17px;font-weight:800;font-style:italic;border-radius:3px}
  .flat-fee{position:absolute;left:0;top:333px;width:100%;text-align:center;font-size:12.5px;font-weight:600;line-height:1.35}
  .flat-fee .hl{color:var(--royal);font-weight:800;font-size:14px}
  .saving{position:absolute;left:0;top:370px;width:100%;text-align:center;font-size:17px;font-weight:800;color:var(--royal)}
  .benefits{position:absolute;left:12px;top:400px;width:326px;border:1.5px solid var(--ink);border-radius:12px;padding:10px 10px 8px 10px;list-style:none;font-family:"Arimo",sans-serif;font-size:10.5px;font-weight:700;line-height:1.3}
  .benefits li{position:relative;padding-left:12px;margin-bottom:7px}
  .benefits li:last-child{margin-bottom:0}
  .benefits li::before{content:"";position:absolute;left:0;top:3px;width:6px;height:6px;background:var(--royal)}
  .example__label{position:absolute;left:104px;top:588px;padding:2px 10px;background:var(--royal);color:var(--white);font-size:13px;font-weight:700}
  .example__box{position:absolute;left:34px;top:606px;width:282px;border:1px solid var(--ink);padding:3px 0;text-align:center;font-size:13px;font-weight:600;line-height:1.35}
  .example__box b{color:var(--royal);font-weight:800}
  .example__note{position:absolute;right:40px;top:652px;font-family:"Arimo",sans-serif;font-size:7.5px;font-style:italic}
  .quote{position:absolute;left:22px;top:676px;width:300px;font-family:"Arimo",sans-serif;font-size:11px;font-style:italic;text-align:center;line-height:1.3}
  .quote__mark{position:absolute;left:-4px;top:-8px;font-family:"Montserrat",sans-serif;font-size:30px;font-style:normal;color:var(--royal)}
  .quote__sig{position:absolute;right:28px;top:730px;text-align:center}
  .quote__sig .sig{font-family:"Satisfy",cursive;font-size:15px}
  .quote__sig .creds{font-family:"Montserrat",sans-serif;font-size:6.5px;font-weight:600}
  .back__brand{position:absolute;left:14px;top:770px;font-size:12px}
  .back__contact{position:absolute;left:140px;top:762px;font-size:12.5px;font-weight:700;line-height:1.45;white-space:nowrap}
  .fine-print{position:absolute;left:38px;top:818px;width:276px;border:1px solid var(--ink);border-radius:4px;padding:3px 6px;text-align:center;font-family:"Arimo",sans-serif;font-size:7px;font-style:italic;line-height:1.25}
</style>
</head>
<body>

<section class="hanger hanger--front" aria-label="Door hanger front">
  <div class="front__sky"></div>
  <div class="photo photo--brick" role="img" aria-label="Photo of a brick two-storey new construction home at dusk"></div>
  <div class="divider divider--one"></div>
  <div class="photo photo--grey" role="img" aria-label="Photo of a grey painted brick home with dark shutters at sunset"></div>
  <div class="divider divider--two"></div>
  <div class="photo photo--white" role="img" aria-label="Photo of a white stucco home with dark roof"></div>

  <h1 class="headline">
    <span class="headline__awe">AWE</span>
    <span class="headline__and">and then</span>
    <span class="headline__some">SOME</span>
  </h1>

  <div class="agent-panel"></div>
  <div class="agent-photo" role="img" aria-label="Portrait of the agent"></div>
  <p class="agent__name">Dana Whitcombe</p>
  <p class="agent__creds">REALTOR®,<br>CRS, ABR, CNHS, CHMS</p>
  <div class="agent__badges"><span class="badge"></span><span class="badge"></span></div>
  <div class="brand front__brand"><span class="brand__mark"></span>Harwood Fenn</div>
  <p class="front__contact"><span class="phone">469.555.0182</span><br>danawhit@mailbox.com</p>

  <div class="hanger__slit"></div>
  <div class="hanger__hole"></div>
</section>

<section class="hanger hanger--back" aria-label="Door hanger back">
  <div class="back__sky" role="img" aria-label="Blue sky with soft clouds"></div>
  <div class="back__content">
    <p class="offer__lead">Receive a minimum of</p>
    <p class="offer__rate">2.5%</p>
    <p class="offer__detail">or more to put<br>towards your<br><b>NEW CONSTRUCTION</b> home!</p>

    <p class="banner">Maximize Your Savings!</p>
    <p class="flat-fee">My <b><i>Buy &amp; List</i></b> package offers a <span class="hl">FLAT<br>FEE</span> on the sale of your current home.</p>
    <p class="saving">SAVING YOU</p>

    <ul class="benefits">
      <li>We work with 100's of builders in the local area so you are not limited to a few "select" builders.</li>
      <li>Homebuilders have the same bottom line sales price whether you have a REALTOR® representing you or not.</li>
      <li>Rebate program will not affect the price you pay for your home. Brokerage fees are paid through a separate marketing fund, not from the sales price of your home.</li>
      <li>Rebate program is in ADDITION to any builder or lender incentives.</li>
    </ul>

    <p class="example__label">For Example:</p>
    <p class="example__box"><b>$400,000</b> equals a <b>$10,000</b> rebate!<br><b>$500,000</b> equals a <b>$12,500</b> rebate!</p>
    <p class="example__note">*Lender approval required</p>

    <blockquote class="quote"><span class="quote__mark">“</span>I've sold hundreds of homes in the North Dallas area over the last 13 years, specializing in new construction homes. I would love to help you make your new home dreams a reality.</blockquote>
    <div class="quote__sig"><p class="sig">Dana Whitcombe</p><p class="creds">REALTOR®, CRS, ABR, CNHS, CHMS</p></div>

    <div class="brand back__brand"><span class="brand__mark"></span>Harwood Fenn</div>
    <p class="back__contact">469.555.0182<br>danawhit@mailbox.com</p>

    <p class="fine-print">Not intended to solicit homes already listed for sale or buyers already in a buyers agency agreement with another brokerage.</p>
  </div>

  <div class="hanger__slit"></div>
  <div class="hanger__hole"></div>
</section>

</body>
</html>
```